Lantern - Web Design Project

We are seeking to have our website redesigned. Our current webpage is rather dated looking www.lantern-outcomes.com We will be utilizing similar content to explain our services as what is in the website now. We do not see it at a retail portal but rather a website for those inquiring about our services as a reference check so to speak.

We wish to have a look that is considered clean, fresh, contemporary and contains a business savvy vibe.

We prefer isolated white background and also wish to retain the integrity of our Logo and colour scheme.

We are looking for something that doesnt look like it was designed at home on sitemoose. We are hoping to find something that looks like it would reside on a tablet.
Updates

Hello designers!

We apologize for our tardiness as we have been quite preoccupied. We will be extending our invites to the end of January!

Hello All,

Please review our offer once again for updated requirements.  We are hoping to accept a design by months end.

Lantern

Target Market(s)

Business to business clients and Large manufacturers

Industry/Entity Type

Retail

Requirements
Must have
• Existing Logo

There must be an area dedicated to an intro video that will be incorporated on our landing page.

We require design of the other pages as well not only the landing page.

```html
<!DOCTYPE html>
<html lang="en">
<head>
<meta charset="utf-8">
<title>Lantern Performance Group</title>
<link href="https://fonts.googleapis.com/css2?family=Open+Sans:wght@400;600&display=swap" rel="stylesheet">
<style>
:root{
  --stage-top:#a5aba8;
  --stage-bottom:#d6d9c8;
  --panel:#ffffff;
  --rule:#dcdcdc;
  --ink:#3a3f44;
  --accent:#8e0a0a;
  --accent-dark:#a31414;
  --band:#f4f4f4;
  --blue:#2e6fae;
  --button:#1f6cc0;
  --footer:#111111;
  --footer-rule:#2a2a2a;
  --muted:#8a8a8a;
  --icon:#4a4a4a;
  --thumb-border:#f27a7a;
}
*{margin:0;padding:0;box-sizing:border-box}
html,body{width:1200px;height:900px;overflow:hidden;background:#fff}
body{position:relative;font-family:Arial,Helvetica,sans-serif}
.stage{position:absolute;left:31px;top:0;width:1124px;height:739px;background:linear-gradient(180deg,var(--stage-top),var(--stage-bottom))}
.page{position:absolute;left:99px;top:0;width:1000px;height:686px;background:var(--panel);box-shadow:0 30px 40px -18px rgba(0,0,0,.55)}
.section-title{position:absolute;left:0;width:1000px;text-align:center;font-family:'Open Sans',sans-serif;font-size:20px;font-weight:600;color:var(--ink);line-height:28px}
.section-title::before{content:"";position:absolute;left:0;right:0;top:10px;border-top:1px solid var(--rule);z-index:0}
.section-title span.wrap{position:relative;z-index:1;background:var(--panel);padding:0 10px}
.section-title em{font-style:normal;color:var(--accent)}
.partners{position:absolute;top:100px;left:0;width:1000px;height:52px}
.partner{position:absolute;top:0;height:52px;display:flex;align-items:center;gap:8px;font-family:'Open Sans',sans-serif;font-weight:600;font-size:20px;transform:translateX(-50%);white-space:nowrap}
.partner i{display:block;width:16px;height:16px}
.newsletter{position:absolute;top:222px;left:0;width:1000px;height:101px;background:radial-gradient(ellipse at center,#fafafa,var(--band));border-top:1px solid var(--rule)}
.quote{position:absolute;left:21px;top:21px;width:450px;font-size:12px;line-height:15px;color:#444}
.quote b{color:#555}
.mail-icon{position:absolute;left:518px;top:27px;width:51px;height:51px;border:1px solid #ccc;background:#fff}
.search{position:absolute;left:695px;top:35px;display:flex}
.search .field{width:214px;height:30px;border:1px solid #c8c8c8;border-radius:3px 0 0 3px;background:#fff;font-size:13px;color:#aaa;padding:7px 8px}
.search .go{width:69px;height:30px;background:linear-gradient(#3586d6,var(--button));border:1px solid #7db24a;color:#fff;font-weight:bold;font-size:14px;text-align:center;line-height:28px;border-radius:0 3px 3px 0}
.footer{position:absolute;top:323px;left:0;width:1000px;height:363px;background:var(--footer);border-top:3px solid var(--blue)}
.col-title{position:absolute;top:29px;width:290px;font-family:'Open Sans',sans-serif;font-size:20px;font-weight:600;color:#fff;line-height:30px;padding-bottom:8px;border-bottom:1px solid var(--footer-rule);box-shadow:0 1px 0 #000}
.col-title em{font-style:normal;color:var(--accent-dark)}
.social-note{position:absolute;left:30px;top:88px;font-size:12px;font-style:italic;color:var(--muted)}
.social{position:absolute;left:30px;top:118px;display:flex;gap:10px}
.social span{width:30px;height:30px;border-radius:50%;background:var(--icon)}
.brand{position:absolute;left:40px;top:172px;font-family:'Open Sans',sans-serif;font-size:44px;font-weight:600;color:#555}
.legal{position:absolute;left:30px;top:256px;font-size:12px;line-height:15px;color:var(--muted)}
.legal a{color:#ddd;text-decoration:none}
.tweet{position:absolute;left:355px;width:290px;height:63px;border-bottom:1px solid #1f1f1f}
.tweet .badge{position:absolute;left:0;top:0;width:35px;height:36px;background:#8d8d8d;border-bottom:1px solid #5fc7d8}
.tweet p{position:absolute;left:55px;top:0;font-size:12px;line-height:15px;color:var(--muted)}
.thumb{position:absolute;width:64px;height:64px;border:2px solid var(--thumb-border)}
</style>
</head>
<body>
<div class="stage"></div>
<div class="page">
  <h2 class="section-title" style="top:47px"><span class="wrap">Our <em>Clients &amp; Partners List</em></span></h2>
  <div class="partners">
    <div class="partner" style="left:108px;color:#c0141b"><i style="background:#c0141b"></i>Harbor Bank</div>
    <div class="partner" style="left:369px;color:#1fa0c8"><i style="background:#1fa0c8"></i>Skyline Systems</div>
    <div class="partner" style="left:626px;color:#e87a1e"><i style="background:#e87a1e;border-radius:50%"></i>Meridian News</div>
    <div class="partner" style="left:888px;color:#4a4a4a"><i style="background:#4a4a4a"></i>Voxora</div>
  </div>
  <h2 class="section-title" style="top:185px"><span class="wrap">Register here <em>For Lantern Performance Group Newsletters</em></span></h2>
  <div class="newsletter">
    <p class="quote">"Those who chase every message in their inbox rarely pause to notice what is really taking shape in the room around them."<br><b>- Anna Verhoeven</b></p>
    <div class="mail-icon">
      <svg width="51" height="51" viewBox="0 0 51 51" aria-hidden="true">
        <rect x="9" y="14" width="33" height="24" fill="#f2c230" stroke="#c9961a"/>
        <path d="M9 14 L25.5 28 L42 14" fill="none" stroke="#c9961a" stroke-width="1.5"/>
        <path d="M14 12 L30 6 L38 13" fill="#7cc04a"/>
      </svg>
    </div>
    <div class="search"><div class="field">Site Search</div><div class="go">submit</div></div>
  </div>
  <div class="footer">
    <h3 class="col-title" style="left:30px">Follow <em>Us on</em></h3>
    <h3 class="col-title" style="left:355px">Chatter <em>Widget</em></h3>
    <h3 class="col-title" style="left:680px">Snapshot <em>Widget</em></h3>
    <p class="social-note">Visit Our Social Network</p>
    <div class="social"><span></span><span></span><span></span><span></span><span></span></div>
    <div class="brand">Lantern</div>
    <p class="legal">© Copyright 2011. All rights reserved.<br>Lantern Performance Group,58 Birchwood Ave N,<br>Kingsley,ON K2P 4R1, Canada &nbsp; T:+1.888.555.0142<br>Email:<a href="#">info@lantern-outcomes.com</a> | &nbsp;<a href="#">Site Map</a></p>
    <div class="tweet" style="top:87px"><span class="badge"></span><p>@ Lantern Performance Group Inc. is the<br>leading provider of profit generating and<br>people development solutions.</p></div>
    <div class="tweet" style="top:163px"><span class="badge"></span><p>@ Lantern Performance Group Inc. is the<br>leading provider of profit generating and<br>people development solutions.</p></div>
    <div class="thumb" role="img" aria-label="Photo: woman with floating photo cards" style="left:680px;top:87px;background:linear-gradient(135deg,#a9c6d8,#e8c9a4)"></div>
    <div class="thumb" role="img" aria-label="Photo: red coffee cup on dark table" style="left:753px;top:87px;background:linear-gradient(135deg,#2a0c0c,#b01818)"></div>
    <div class="thumb" role="img" aria-label="Photo: tablet with app tiles" style="left:826px;top:87px;background:linear-gradient(135deg,#3a4656,#6fa0c8)"></div>
    <div class="thumb" role="img" aria-label="Illustration: globe and clock" style="left:899px;top:87px;background:linear-gradient(135deg,#ffffff,#2f6cc4)"></div>
    <div class="thumb" role="img" aria-label="Photo: man using touch interface" style="left:680px;top:160px;background:linear-gradient(135deg,#7fa4b8,#2c3e4e)"></div>
    <div class="thumb" role="img" aria-label="Photo: woman drawing a diagram" style="left:753px;top:160px;background:linear-gradient(135deg,#f4ede6,#c9a48a)"></div>
    <div class="thumb" role="img" aria-label="Photo: businessman pressing a glowing button" style="left:826px;top:160px;background:linear-gradient(135deg,#1c2436,#6a7fa6)"></div>
    <div class="thumb" role="img" aria-label="Photo: woman looking at screens" style="left:899px;top:160px;background:linear-gradient(135deg,#a6a29a,#5a5048)"></div>
    <div class="thumb" role="img" aria-label="Photo: two colleagues at a desk" style="left:680px;top:233px;background:linear-gradient(135deg,#d8d2c8,#4a3e36)"></div>
  </div>
</div>
</body>
</html>
```